New Alcoholic Spiked Seltzer Line

We need a can design for a line of low calorie alcoholic seltzer. This product is a sparkling water and vodka drink with no sugar added in a slim 12 oz can.

This is a lighter, healthier, alternative to the sugary ready-to-drinks on the market. The product contains only 3 ingredients: Vodka, Water and Natural Flavors. It has only 100 calories but still has 5% alcohol, so you don't need to sacrifice alcohol to cut calories.

This product also does not contain any preservatives.

We want this design to communicate the following objectives to the consumer and in this order:

1. Appetizing product
2.Low calorie
3.Communicate the type of beverage (Spiked Seltzer)

The brand name of the product is VELKA.

The flavor of the product needed to be used for the design is Mango-Orange.

Comparable products are:

www.brisavelfizz.example/
https://www.tarnowbubble.example
https://quellrind.example/

The designs should not infringe or copy the creative directions of the products mentionned above. They are only given so that you can better understand the type of product we are developing.

Target Market(s)

Young Professional women between the ages of 25 and 44

Industry/Entity Type

Product

Colors

Designer to choose colors to be used in the design.

Requirements
Must have
• Design extendibility, meaning it can be adapted for other flavors.
• This is a new category in the market we are targeting, so consumers must easily be able to identify what type of product this is.

```html
<!DOCTYPE html>
<html lang="en">
<head>
<meta charset="utf-8">
<title>VELKA Mango and Orange Spiked Seltzer – Can Label</title>
<link rel="stylesheet" href="https://fonts.googleapis.com/css2?family=Oswald:wght@300;500;700&display=swap">
<style>
  :root {
    --backdrop: #e9e9e9;
    --label-white: #ffffff;
    --band-black: #111111;
    --citrus-orange: #f08a12;
    --citrus-orange-deep: #e27a06;
    --citrus-orange-light: #f7a531;
    --ink: #141414;
    --fruit-tone-a: #f7b334;
    --fruit-tone-b: #e9a12a;
  }
  * { box-sizing: border-box; margin: 0; padding: 0; }
  html, body {
    width: 1200px;
    height: 960px;
    overflow: hidden;
    background: var(--backdrop);
  }
  .canvas {
    position: relative;
    width: 1200px;
    height: 960px;
    display: flex;
    align-items: center;
    justify-content: center;
  }
  .can-label {
    position: relative;
    width: 360px;
    height: 880px;
    background: var(--label-white);
    overflow: hidden;
    font-family: "Oswald", "Arial Narrow", sans-serif;
  }
  .label-top {
    position: absolute;
    left: 0; top: 0;
    width: 100%;
    height: 568px;
    background: var(--label-white);
  }
  .brand-block {
    position: absolute;
    left: 40px;
    top: 190px;
    width: 290px;
  }
  .brand-row {
    display: flex;
    align-items: flex-start;
    gap: 8px;
  }
  .brand-name {
    font-weight: 700;
    font-size: 96px;
    line-height: 1;
    letter-spacing: 1px;
    color: var(--ink);
  }
  .brand-dot {
    width: 26px;
    height: 26px;
    border-radius: 50%;
    background: var(--citrus-orange);
    margin-top: 4px;
  }
  .tagline {
    margin-top: 6px;
    font-weight: 500;
    font-size: 15.5px;
    letter-spacing: 0.2px;
    color: var(--citrus-orange);
    text-transform: uppercase;
    white-space: nowrap;
  }
  .label-band {
    position: absolute;
    left: 0;
    top: 568px;
    width: 100%;
    height: 18px;
    background: var(--band-black);
  }
  .label-bottom {
    position: absolute;
    left: 0;
    top: 586px;
    width: 100%;
    height: 294px;
    background: linear-gradient(180deg, var(--citrus-orange-light) 0%, var(--citrus-orange) 45%, var(--citrus-orange-deep) 100%);
  }
  .label-bottom svg.swoosh {
    position: absolute;
    inset: 0;
  }
  .fruit-art {
    position: absolute;
    left: 82px;
    top: 92px;
    width: 132px;
    height: 68px;
    border-radius: 34px 34px 20px 20px;
    background: linear-gradient(135deg, var(--fruit-tone-a), var(--fruit-tone-b));
  }
  .flavor-name {
    position: absolute;
    left: 78px;
    top: 188px;
    font-weight: 700;
    font-size: 19px;
    color: var(--ink);
    text-transform: uppercase;
    letter-spacing: 0.2px;
  }
  .abv {
    position: absolute;
    left: 244px;
    top: 118px;
    font-weight: 300;
    font-size: 60px;
    line-height: 1;
    color: var(--ink);
  }
</style>
</head>
<body>
  <main class="canvas">
    <section class="can-label" aria-label="VELKA Mango and Orange can label">
      <div class="label-top">
        <div class="brand-block">
          <div class="brand-row">
            <span class="brand-name">VELKA</span>
            <span class="brand-dot" aria-hidden="true"></span>
          </div>
          <p class="tagline">Vodka, water and natural flavors</p>
        </div>
      </div>
      <div class="label-band"></div>
      <div class="label-bottom">
        <svg class="swoosh" width="360" height="294" viewBox="0 0 360 294" aria-hidden="true">
          <path d="M150 0 C 230 60, 230 150, 360 170 L360 0 Z" fill="#ffffff" fill-opacity="0.06"/>
          <path d="M250 0 C 290 80, 320 100, 360 110 L360 0 Z" fill="#ffffff" fill-opacity="0.05"/>
        </svg>
        <div class="fruit-art" role="img" aria-label="Illustration of an orange wedge with sliced mango pieces"></div>
        <p class="flavor-name">Mango and Orange</p>
        <p class="abv">5%</p>
      </div>
    </section>
  </main>
</body>
</html>
```